Personal Finance e-commerce website needs a simple budget design

Hello! I am starting to sell downloadable and printable budget planners, as shown in the attached file, for people to plan ahead on their personal finances. <br/><br/>I want to see a one-page design with similar columns (for example, "Expenses, Budget, and Actual"). I would also like to see the basic formula ("Net Income = Gross income - Total Expenses") somewhere on the design. Finally, I want the design to remain mostly minimalistic and simple for the average person to plan their personal monthly budgets.<br/><br/>However, other than that, the overall design, layout, and colors will be at the graphic designer's choice. If you have any questions for me, please let me know. Thank you for your time!

Industry/Entity Type

Financial Planning

Colors

Designer to choose colors to be used in the design.

Requirements
Must have
• I want to see a one-page design with similar columns (for example, "Expenses, Budget, and Actual").
• I want the design to remain mostly minimalistic and simple for the average person to plan their personal monthly budgets.
Nice to have
• I would also like to see the basic formula ("Net Income = Gross income - Total Expenses") somewhere on the design.

```html
<!DOCTYPE html>
<html lang="en">
<head>
<meta charset="utf-8">
<title>Basic Monthly Budget Planner</title>
<link href="https://fonts.googleapis.com/css2?family=Mulish:wght@400;600&family=Stardos+Stencil:wght@700&family=Cinzel:wght@600&display=swap" rel="stylesheet">
<style>
  :root {
    --page-bg: #ffffff;
    --sheet: #ffffff;
    --grad-left: #9a73b8;
    --grad-right: #e14c9c;
    --ink: #2b2b2b;
    --title-dark: #2a2a2a;
    --expenses: #b01f2a;
    --budget: #8aab3c;
    --actual: #5a4d6a;
    --sub-grey: #dcdcdc;
    --foot-grey: #dedfe0;
    --rule: #c9c9c9;
    --rule-budget: #e6ecc8;
    --orange: #f39a22;
    --green: #3bb44a;
    --pink: #e23a68;
  }
  * { margin: 0; padding: 0; box-sizing: border-box; }
  html, body { width: 1200px; height: 955px; overflow: hidden; background: var(--page-bg); }
  body { position: relative; font-family: "Mulish", sans-serif; color: var(--ink); }

  .sheet { position: absolute; left: 289px; top: 43px; width: 600px; height: 847px; background: var(--sheet); }

  .header { position: absolute; left: 0; top: 0; width: 600px; height: 142px;
    background: linear-gradient(90deg, var(--grad-left), var(--grad-right)); }
  .brand { position: absolute; left: 30px; top: 12px; width: 124px; height: 124px; border-radius: 50%;
    background: #fff; display: flex; align-items: center; justify-content: center; text-align: center;
    font-family: "Mulish", sans-serif; font-weight: 400; font-size: 22px; line-height: 24px; color: var(--ink); letter-spacing: 1px; }
  .title-top { position: absolute; left: 238px; top: 10px; width: 276px; text-align: center;
    font-family: "Stardos Stencil", serif; font-weight: 700; font-size: 38px; color: #fff; font-variant: small-caps; letter-spacing: 0.5px; }
  .title-main { position: absolute; left: 210px; top: 46px; width: 340px; text-align: center;
    font-family: "Cinzel", serif; font-weight: 600; font-size: 30px; color: var(--title-dark); letter-spacing: 0.5px; }
  .date-field { position: absolute; left: 258px; top: 88px; width: 235px; height: 28px; background: #fff; border-radius: 6px; }
  .date-label { position: absolute; top: 118px; font-size: 13px; color: #fff; }
  .date-label.month { left: 301px; }
  .date-label.year { left: 403px; }

  .column { position: absolute; top: 148px; width: 183px; }
  .column.expenses { left: 14px; }
  .column.budget { left: 208px; }
  .column.actual { left: 402px; }
  .col-head { height: 29px; color: #fff; font-size: 17px; text-align: center; line-height: 29px; }
  .expenses .col-head { background: var(--expenses); }
  .budget .col-head { background: var(--budget); }
  .actual .col-head { background: var(--actual); }
  .col-sub { margin-top: 4px; height: 19px; background: var(--sub-grey); font-size: 13px; text-align: center; line-height: 19px; }
  .col-rows { height: 518px; border: 1px solid var(--rule); border-top: none;
    background: repeating-linear-gradient(180deg, transparent 0 23.7px, var(--rule) 23.7px 24.7px); }
  .budget .col-rows { background: repeating-linear-gradient(180deg, transparent 0 23.7px, var(--rule-budget) 23.7px 24.7px); }
  .col-total { margin-top: 1px; height: 35px; background: var(--foot-grey); }

  .formula-pill { position: absolute; top: 763px; height: 36px; border-radius: 18px; color: #fff;
    font-size: 17px; display: flex; align-items: center; }
  .formula-pill svg { margin-left: 4px; margin-right: 10px; }
  .pill-net { left: 19px; width: 163px; background: var(--orange); }
  .pill-gross { left: 225px; width: 151px; background: var(--green); font-size: 16px; }
  .pill-total { left: 416px; width: 156px; background: var(--pink); font-size: 16px; }
  .operator { position: absolute; top: 763px; }
  .op-equals { left: 191px; }
  .op-minus { left: 384px; }
  .pill-note { position: absolute; top: 803px; font-size: 12.5px; line-height: 12px; text-align: center; color: var(--ink); }
  .note-net { left: 30px; width: 142px; }
  .note-gross { left: 228px; width: 142px; }
  .note-total { left: 430px; width: 140px; top: 808px; }

  .foot-band { position: absolute; left: 0; bottom: 0; width: 600px; height: 8px;
    background: linear-gradient(90deg, var(--grad-left), var(--grad-right)); }
</style>
</head>
<body>
  <main class="sheet">
    <header class="header">
      <div class="brand">NORA<br>VELL</div>
      <h1 class="title-top">Basic Monthly</h1>
      <h2 class="title-main">Budget Planner</h2>
      <div class="date-field"></div>
      <span class="date-label month">Month</span>
      <span class="date-label year">Year</span>
    </header>

    <section class="column expenses">
      <div class="col-head">Expenses</div>
      <div class="col-sub">Custom category</div>
      <div class="col-rows"></div>
      <div class="col-total"></div>
    </section>
    <section class="column budget">
      <div class="col-head">Budget (USD)</div>
      <div class="col-sub">What you plan to spend</div>
      <div class="col-rows"></div>
      <div class="col-total"></div>
    </section>
    <section class="column actual">
      <div class="col-head">Actual (USD)</div>
      <div class="col-sub">What you actualy spent</div>
      <div class="col-rows"></div>
      <div class="col-total"></div>
    </section>

    <div class="formula-pill pill-net">
      <svg width="30" height="30" viewBox="0 0 30 30"><circle cx="15" cy="15" r="14" fill="#fff"/><circle cx="15" cy="15" r="10" fill="none" stroke="#9aa2a8" stroke-width="2"/><text x="15" y="20" text-anchor="middle" font-family="Mulish, sans-serif" font-size="14" font-weight="600" fill="#3bb44a">$</text></svg>
      Net Income
    </div>
    <svg class="operator op-equals" width="20" height="36" viewBox="0 0 20 36"><rect x="1" y="11" width="18" height="4" fill="#3bb44a"/><rect x="1" y="20" width="18" height="4" fill="#3bb44a"/></svg>
    <div class="formula-pill pill-gross">
      <svg width="30" height="30" viewBox="0 0 30 30"><circle cx="15" cy="15" r="14" fill="#fff"/><circle cx="15" cy="15" r="10" fill="none" stroke="#9aa2a8" stroke-width="2"/><text x="15" y="20" text-anchor="middle" font-family="Mulish, sans-serif" font-size="14" font-weight="600" fill="#3bb44a">$</text></svg>
      Gross Income
    </div>
    <svg class="operator op-minus" width="24" height="36" viewBox="0 0 24 36"><rect x="1" y="11" width="22" height="13" rx="4" fill="#e23a68"/><rect x="6" y="16" width="12" height="3" fill="#fff"/></svg>
    <div class="formula-pill pill-total">
      <svg width="30" height="30" viewBox="0 0 30 30"><circle cx="15" cy="15" r="14" fill="#fff"/><text x="15" y="21" text-anchor="middle" font-family="Mulish, sans-serif" font-size="17" font-weight="600" fill="#3bb44a">$</text></svg>
      Total Expenses
    </div>
    <p class="pill-note note-net">How much money<br>you kept</p>
    <p class="pill-note note-gross">How much money<br>you earned</p>
    <p class="pill-note note-total">Actual Expenses</p>

    <div class="foot-band"></div>
  </main>
</body>
</html>
```